Need business card designed for a Mobile RV Repair business

I need a business card designed

Welding sparks

Industry/Entity Type

Rv Repair , Mobile Welding & Fabrication

Contact Information for Business Card

****

Colors
0054AA
0677BA
7BADD7
CADEEF
E8F1F8

Requirements
Nice to have
• welding sparks, list of services, welding vector

```html
<!DOCTYPE html>
<html lang="en">
<head>
<meta charset="utf-8">
<title>Ridgeway Mobile – Business Card</title>
<link rel="stylesheet" href="https://fonts.googleapis.com/css2?family=Lato:wght@400;700;900&display=swap">
<style>
  :root{
    --blue-deep:#0054aa;
    --blue-mid:#0677ba;
    --blue-soft:#7badd7;
    --blue-pale:#cadeef;
    --blue-mist:#e8f1f8;
    --white:#ffffff;
    --ink:#1a1a1a;
    --stage:#2b2c2e;
    --silver-a:#a9abae;
    --silver-b:#e9eaeb;
  }
  *{margin:0;padding:0;box-sizing:border-box}
  html,body{width:1200px;height:1122px;overflow:hidden;background:var(--stage)}
  body{font-family:"Lato",sans-serif;position:relative}

  .card{position:absolute;left:180px;width:840px;height:480px;border-radius:28px;overflow:hidden;background:var(--white)}
  .card--services{top:56px}
  .card--contact{top:586px}

  .card__shape{position:absolute;inset:0}

  /* services side */
  .services{position:absolute;left:48px;top:92px;list-style:none;color:var(--white)}
  .services li{font-weight:700;font-size:22px;letter-spacing:.5px;line-height:36px;text-transform:uppercase;display:flex;align-items:center;gap:12px;white-space:nowrap}
  .services svg{width:16px;height:16px;flex:none}

  .photo{position:absolute;border-radius:16px}
  .photo--frames{left:400px;top:40px;width:195px;height:150px;background:linear-gradient(135deg,#c9ccd0,#8d9196)}
  .photo--trailer-open{left:610px;top:22px;width:205px;height:120px;background:linear-gradient(135deg,#dfe3e8,#a6adb5)}
  .photo--trailer-side{left:612px;top:154px;width:206px;height:132px;background:linear-gradient(135deg,#e8edf2,#b5bcc4)}
  .photo--interior{left:400px;top:202px;width:198px;height:130px;background:linear-gradient(135deg,#4a4d52,#c5c8cc)}
  .photo--owner{left:612px;top:298px;width:206px;height:162px;background:linear-gradient(160deg,#9cc3ea,#e6eef5)}
  .photo--motorhome{left:400px;top:344px;width:198px;height:118px;background:linear-gradient(135deg,#dfe6ee,#9fb0c2)}

  /* contact side */
  .brand{position:absolute;left:44px;top:172px;color:var(--blue-deep);white-space:nowrap}
  .brand__name{font-weight:900;font-size:34px;letter-spacing:.5px;line-height:1}
  .brand__tagline{font-weight:900;font-size:17px;margin-top:9px;letter-spacing:.4px}
  .brand__services{font-weight:700;font-size:10.5px;margin-top:7px;color:var(--blue-mid);letter-spacing:.7px}

  .person{position:absolute;left:536px;top:192px;white-space:nowrap}
  .person__name{font-weight:900;font-size:36px;color:var(--blue-deep);letter-spacing:.5px;line-height:1}
  .person__role{font-weight:400;font-size:22px;color:var(--ink);margin-top:8px}

  .contact{position:absolute;left:550px;top:336px;list-style:none;color:var(--white);white-space:nowrap}
  .contact li{display:flex;align-items:center;gap:12px;line-height:44px}
  .contact__phone{font-size:28px;font-weight:400;letter-spacing:.5px}
  .contact__email{font-size:19px;font-weight:400}
  .contact svg{width:22px;height:22px;flex:none}
</style>
</head>
<body>

<section class="card card--services" aria-label="Business card, services side">
  <svg class="card__shape" viewBox="0 0 840 480" aria-hidden="true">
    <polygon points="0,0 392,0 372,480 0,480" fill="var(--blue-deep)"/>
  </svg>

  <ul class="services">
    <li><svg viewBox="0 0 16 16"><polygon points="8,0 10,6 16,8 10,10 8,16 6,10 0,8 6,6" fill="#fff"/></svg>RV Repair</li>
    <li><svg viewBox="0 0 16 16"><polygon points="8,0 10,6 16,8 10,10 8,16 6,10 0,8 6,6" fill="#fff"/></svg>Electrical</li>
    <li><svg viewBox="0 0 16 16"><polygon points="8,0 10,6 16,8 10,10 8,16 6,10 0,8 6,6" fill="#fff"/></svg>Plumbing</li>
    <li><svg viewBox="0 0 16 16"><polygon points="8,0 10,6 16,8 10,10 8,16 6,10 0,8 6,6" fill="#fff"/></svg>General Repairs</li>
    <li><svg viewBox="0 0 16 16"><polygon points="8,0 10,6 16,8 10,10 8,16 6,10 0,8 6,6" fill="#fff"/></svg>Mobile Welding</li>
    <li><svg viewBox="0 0 16 16"><polygon points="8,0 10,6 16,8 10,10 8,16 6,10 0,8 6,6" fill="#fff"/></svg>Custom Fabrication</li>
    <li><svg viewBox="0 0 16 16"><polygon points="8,0 10,6 16,8 10,10 8,16 6,10 0,8 6,6" fill="#fff"/></svg>Gates/Fences</li>
    <li><svg viewBox="0 0 16 16"><polygon points="8,0 10,6 16,8 10,10 8,16 6,10 0,8 6,6" fill="#fff"/></svg>Aluminum Welding</li>
  </ul>

  <div class="photo photo--frames" role="img" aria-label="Photo of welded trailer frames"></div>
  <div class="photo photo--trailer-open" role="img" aria-label="Photo of a white cargo trailer with open door"></div>
  <div class="photo photo--trailer-side" role="img" aria-label="Photo of a finished trailer side view"></div>
  <div class="photo photo--interior" role="img" aria-label="Photo of a fitted trailer interior"></div>
  <div class="photo photo--owner" role="img" aria-label="Photo of the owner at a work site"></div>
  <div class="photo photo--motorhome" role="img" aria-label="Photo of a repaired motorhome"></div>
</section>

<section class="card card--contact" aria-label="Business card, contact side">
  <svg class="card__shape" viewBox="0 0 840 480" aria-hidden="true">
    <defs>
      <linearGradient id="silver-band" x1="0" y1="0" x2="1" y2="0">
        <stop offset="0" stop-color="var(--silver-a)"/>
        <stop offset=".55" stop-color="var(--silver-b)"/>
        <stop offset=".8" stop-color="var(--silver-a)"/>
        <stop offset="1" stop-color="var(--silver-b)"/>
      </linearGradient>
    </defs>
    <polygon points="508,0 840,0 840,480 520,480" fill="var(--blue-deep)"/>
    <polygon points="470,152 840,152 840,306 470,306" fill="url(#silver-band)"/>
    <polygon points="470,152 512,140 512,152" fill="#8e9093"/>
  </svg>

  <div class="brand">
    <div class="brand__name">RIDGEWAY MOBILE</div>
    <div class="brand__tagline">RV &amp; MOTORHOME REPAIR</div>
    <div class="brand__services">RV REPAIR, ELECTRICAL, PLUMBING, ROOF REPAIR AND MORE!</div>
  </div>

  <div class="person">
    <div class="person__name">DEAN MARLOW</div>
    <div class="person__role">Owner</div>
  </div>

  <ul class="contact">
    <li class="contact__phone">
      <svg viewBox="0 0 24 24"><path d="M6.6 10.8a15 15 0 0 0 6.6 6.6l2.2-2.2c.3-.3.7-.4 1-.2 1.1.4 2.3.6 3.6.6.6 0 1 .4 1 1V20c0 .6-.4 1-1 1A17 17 0 0 1 3 4c0-.6.4-1 1-1h3.5c.6 0 1 .4 1 1 0 1.2.2 2.4.6 3.6.1.3 0 .7-.2 1z" fill="#fff"/></svg>
      555.204.7781
    </li>
    <li class="contact__email">
      <svg viewBox="0 0 24 24"><rect x="2" y="5" width="20" height="14" fill="#fff"/><polyline points="2,5 12,13 22,5" fill="none" stroke="var(--blue-deep)" stroke-width="1.6"/></svg>
      ridgewayrv@example.com
    </li>
  </ul>
</section>

</body>
</html>
```